Quorvane Capital Modern Business Card

We need a modern business card template designed for Quorvane Capital.
Quorvane Capital is a diversified global cryptocurrency investment fund.

The font under the logo: Hiragino Kaku Gothic Pro

Color Hexcode: Main colors white (ffffff) & teal (188383), we are open to adding #fcca46 as an accent

Target Market(s)

Accredited Investors, high net worth individuals and institutional investors

Industry/Entity Type

Investment

Contact Information for Business Card

Contact Information should contain
Name
main phone +1 720 555 0147
cell
email

Font styles to use
Sans Serif
Other font styles liked:
• Hiragino Kaku Gothic Pro

Requirements
Must have
• would like to have icons that identify the contact information
• include our website: www.quorvanecapital.example
• include our Tagline: Diversified Crypto Investment Funds
Nice to have
• Would like to have a simple back side with the logo (without the words) and plenty of space

```html
<!DOCTYPE html>
<html lang="en">
<head>
<meta charset="utf-8">
<title>Quorvane Capital – Business Card</title>
<link href="https://fonts.googleapis.com/css2?family=Noto+Sans+JP:wght@300;400;700&display=swap" rel="stylesheet">
<style>
  :root {
    --teal: #188383;
    --teal-light: #1f9696;
    --teal-dark: #136b6b;
    --white: #ffffff;
    --ink: #222222;
    --stripe: #2a2a2a;
    --page: #ecefef;
    --font: "Noto Sans JP", "Hiragino Kaku Gothic Pro", sans-serif;
  }
  * { box-sizing: border-box; margin: 0; padding: 0; }
  html, body {
    width: 1200px; height: 1200px; overflow: hidden;
    background: var(--page);
    font-family: var(--font);
  }
  .canvas {
    width: 1200px; height: 1200px;
    display: flex; flex-direction: column;
    align-items: center; justify-content: center; gap: 60px;
  }
  .card {
    position: relative;
    width: 900px; height: 514px;
    overflow: hidden;
    box-shadow: 0 10px 30px rgba(0,0,0,0.12);
  }

  /* Back side */
  .card--back {
    background: linear-gradient(135deg, var(--teal-light) 0%, var(--teal) 50%, var(--teal-dark) 100%);
    display: flex; align-items: center; justify-content: center;
  }
  .wordmark {
    font-weight: 300;
    letter-spacing: 0.04em;
    text-transform: uppercase;
    white-space: nowrap;
  }
  .card--back .wordmark { color: var(--white); font-size: 52px; }

  /* Front side */
  .card--front { background: var(--white); }
  .front-shape { position: absolute; inset: 0; width: 100%; height: 100%; }
  .brand {
    position: absolute; left: 60px; top: 262px;
  }
  .brand .wordmark { color: var(--ink); font-size: 34px; line-height: 1.1; }
  .brand-mark {
    display: inline-block; width: 18px; height: 18px;
    background: var(--teal); margin-right: 12px; vertical-align: 3px;
  }
  .tagline {
    margin-top: 8px;
    font-size: 19px; font-weight: 400; color: var(--ink);
    letter-spacing: 0.02em;
  }
  .person {
    position: absolute; right: 48px; top: 48px;
    text-align: right; color: var(--white);
  }
  .person-name { font-size: 34px; font-weight: 700; letter-spacing: 0.02em; line-height: 1; text-transform: uppercase; }
  .person-role { font-size: 18px; font-weight: 400; margin-top: 4px; }
  .contacts {
    list-style: none;
    position: absolute; right: 48px; top: 180px;
    color: var(--white); font-size: 16px; font-weight: 300;
  }
  .contacts li {
    display: flex; align-items: center; justify-content: flex-end;
    gap: 12px; height: 32px;
  }
  .contacts svg { width: 18px; height: 18px; flex: none; }
</style>
</head>
<body>
<main class="canvas">

  <section class="card card--back" aria-label="Business card back">
    <span class="wordmark">Quorvane Capital</span>
  </section>

  <section class="card card--front" aria-label="Business card front">
    <svg class="front-shape" viewBox="0 0 900 514" preserveAspectRatio="none" aria-hidden="true">
      <defs>
        <linearGradient id="panelFill" x1="0" y1="0" x2="1" y2="1">
          <stop offset="0" stop-color="#1f9696"/>
          <stop offset="1" stop-color="#136b6b"/>
        </linearGradient>
      </defs>
      <polygon points="616,0 900,0 900,514 496,514" fill="url(#panelFill)"/>
      <polygon points="596,0 616,0 496,514 476,514" fill="#2a2a2a"/>
    </svg>

    <div class="brand">
      <div class="wordmark"><span class="brand-mark"></span>Quorvane Capital</div>
      <p class="tagline">Diversified Crypto Investment Funds</p>
    </div>

    <div class="person">
      <p class="person-name">Dana Reyes</p>
      <p class="person-role">Manager</p>
    </div>

    <ul class="contacts">
      <li>+1 720 555 0147
        <svg viewBox="0 0 24 24" fill="#ffffff" aria-hidden="true"><path d="M6.6 10.8c1.4 2.8 3.8 5.1 6.6 6.6l2.2-2.2c.3-.3.7-.4 1-.2 1.1.4 2.3.6 3.6.6.6 0 1 .4 1 1V20c0 .6-.4 1-1 1C10.6 21 3 13.4 3 4c0-.6.4-1 1-1h3.5c.6 0 1 .4 1 1 0 1.3.2 2.5.6 3.6.1.3 0 .7-.2 1l-2.3 2.2z"/></svg>
      </li>
      <li>+1 720 555 0193
        <svg viewBox="0 0 24 24" fill="none" stroke="#ffffff" stroke-width="1.8" aria-hidden="true"><rect x="7" y="2.5" width="10" height="19" rx="2"/><path d="M11 18.5h2"/></svg>
      </li>
      <li>hello@quorvanecapital.example
        <svg viewBox="0 0 24 24" fill="#ffffff" aria-hidden="true"><path d="M3 5h18c.6 0 1 .4 1 1v12c0 .6-.4 1-1 1H3c-.6 0-1-.4-1-1V6c0-.6.4-1 1-1zm9 7.2L4.2 7v.2L12 13l7.8-5.8V7L12 12.2z"/></svg>
      </li>
      <li>www.quorvanecapital.example
        <svg viewBox="0 0 24 24" fill="none" stroke="#ffffff" stroke-width="1.8" aria-hidden="true"><circle cx="12" cy="12" r="9"/><path d="M3 12h18M12 3c2.5 2.6 3.8 5.6 3.8 9s-1.3 6.4-3.8 9c-2.5-2.6-3.8-5.6-3.8-9S9.5 5.6 12 3z"/></svg>
      </li>
    </ul>
  </section>

</main>
</body>
</html>
```